Modern, clean and professional Wordpress design for a safety training company!

We are currently in the process of creating a new website for our business. We have hired a website developer and the main structure of our new Wordpress site is complete. We now need an overall design plan for the site. We need a very clean, professional and easy to follow website. Most of our website visitors only spend about 30-45 secs on our sites "shopping " so it is imperative that we have a strong Home Page.
Our company specializes in CPR and First Aid Certification Classes to businesses and individuals throughout Northern California. We provide these certifications two ways: ONSITE-We come to you, and HOSTED-we offer weekly classes at our 2 locations.
Our design needs to use the general green and blue colors of our logo. But we also like white.
The final design MUST communicate a legitimate, trustworthy and professional business. Our industry is VERY competitive and we need to STAND OUT.
Currently, the NEW website that we need a new design for is www.LifelineSkillsHub.com
Our old website is www.RescueCoursesValley.com and we really do like the design of this website, but we just needed a Wordpress site for SEO purposes.
These are 3 websites that we really:
http://vorlandmedix.com/
http://www.pelbrik.com/
https://www.quimby.com/
I have attached our Logo and other images if you need to use them but looking at the current two sites will be you best help.
1) Large businesses and industries that are looking for a company to provide ONSITE safety training classes at their office or place of work.
2) Individuals that need certifications for their jobs and other needs. These individuals are looking for a legitimate, trustworthy and professional environment to complete their training class.

```html
<!DOCTYPE html>
<html lang="en">
<head>
<meta charset="utf-8">
<title>Harbor Safety Institute – CPR &amp; First Aid</title>
<link href="https://fonts.googleapis.com/css2?family=Oswald:wght@400;500&family=Open+Sans:wght@400;600;700&display=swap" rel="stylesheet">
<style>
:root{
  --blue:#2454a5;
  --blue-dark:#173b7c;
  --blue-deep:#102d63;
  --green:#7cb645;
  --green-dark:#5d9a2c;
  --ink:#333a44;
  --muted:#6d7480;
  --paper:#ffffff;
  --mist:#eef2f6;
  --line:#d7dde5;
}
*{margin:0;padding:0;box-sizing:border-box}
html,body{width:771px;height:1200px;overflow:hidden}
body{position:relative;background:var(--mist);font-family:"Open Sans",Arial,sans-serif;color:var(--ink);font-size:7px;line-height:1.45}
.abs{position:absolute}
h1,h2,h3,h4{font-family:"Oswald","Arial Narrow",sans-serif;font-weight:400;text-transform:uppercase}

/* header */
.site-header{left:0;top:0;width:771px;height:51px;background:var(--paper);border-bottom:3px solid var(--green)}
.brand{left:100px;top:6px;display:flex;align-items:center;gap:7px}
.brand-dot{width:34px;height:34px;border-radius:50%;background:var(--blue)}
.brand-name{font-family:"Open Sans",sans-serif;font-weight:700;color:var(--blue);font-size:13px;line-height:1.05}
.main-nav{left:308px;top:8px;display:flex;gap:10px;font-size:6px;font-weight:600;color:var(--blue-dark);text-transform:uppercase}
.social{top:6px;display:flex;gap:5px}
.social span{display:block;width:10px;height:10px;border-radius:2px;background:var(--blue)}
.header-contact{left:470px;top:27px;font-size:6.5px;color:var(--muted);display:flex;gap:16px}
.header-contact b{color:var(--blue-dark)}

/* hero */
.hero{left:0;top:54px;width:771px;height:326px;background:linear-gradient(100deg,#2c3b52 0%,#56667d 35%,#b8c2cf 65%,#d7dde4 100%)}
.hero-title{left:128px;top:196px;color:#fff;font-size:31px;letter-spacing:1px;font-weight:400}
.hero-sub{left:128px;top:238px;background:var(--blue);color:#fff;font-family:"Oswald",sans-serif;font-size:9px;letter-spacing:1px;padding:2px 8px}
.hero-btn{left:128px;top:258px;background:var(--blue-dark);color:#fff;font-size:6.5px;font-weight:700;padding:5px 11px;text-transform:uppercase;border-radius:2px}
.dots{left:372px;top:366px;display:flex;gap:4px}
.dots span{width:5px;height:5px;border-radius:50%;background:#fff;opacity:.6}
.dots span:first-child{opacity:1;background:var(--green)}

/* content wrap */
.wave{left:0;top:372px}
.content{left:106px;top:438px;width:560px;height:594px;background:var(--paper)}

.card{top:460px;width:172px}
.card .ph{height:94px;background:linear-gradient(135deg,#8fa1b6,#c8d1dc);border:3px solid var(--paper);box-shadow:0 0 0 1px var(--line)}
.card h3{margin-top:5px;font-size:9.5px;color:var(--blue);border-bottom:2px solid var(--green);padding-bottom:2px}
.card p{margin-top:4px;color:var(--muted);font-size:5.5px}
.more{color:var(--blue);font-weight:700;font-size:5.5px;margin-top:4px;display:block}

.welcome{left:120px;top:628px;width:340px}
.welcome h2,.testimonials h2{font-size:13px;color:var(--blue);padding-bottom:3px;border-bottom:1px solid var(--line)}
.welcome h2 em,.testimonials h2 em{font-style:normal;color:var(--green)}
.welcome p{margin-top:6px;font-size:6.2px;color:var(--muted)}
.welcome p b{color:var(--ink)}
.testimonials{left:482px;top:628px;width:172px}
.quote{margin-top:8px;display:flex;gap:6px;align-items:center}
.avatar{width:22px;height:22px;border-radius:50%;background:#c4ccd6}
.quote-name{color:var(--blue);font-weight:700;font-size:6.5px}
.quote-role{color:var(--muted);font-size:5px}
.bubble{margin-top:6px;background:var(--mist);border:1px solid var(--line);padding:6px;font-size:5.5px;color:var(--muted);border-radius:3px}

.service{top:782px;width:262px;height:214px;display:flex;gap:6px}
.service .ph{width:128px;height:214px;background:linear-gradient(160deg,#a9b6c5,#dde3ea);border:3px solid var(--paper);box-shadow:0 0 0 1px var(--line)}
.service .txt{width:128px;border-top:3px solid var(--green);padding-top:4px}
.service h3{font-size:16px;color:var(--blue)}
.service p{margin-top:5px;font-size:5.8px;color:var(--muted)}
.service p b{color:var(--ink)}
.service .btn{display:inline-block;margin-top:8px;background:var(--green);color:#fff;font-size:5.5px;font-weight:700;padding:3px 8px;border-radius:2px}

/* footer */
.site-footer{left:0;top:1036px;width:771px;height:164px;background:linear-gradient(180deg,var(--blue) 0%,var(--blue-deep) 100%)}
.footer-wave{left:0;top:1028px}
.f-col{top:1054px;color:#fff}
.f-col h4{font-size:11px;letter-spacing:.5px;margin-bottom:8px}
.f-links li{list-style:none;font-size:5.8px;margin-bottom:3px;color:#d5e0f3}
.f-links li::before{content:"› ";color:var(--green)}
.field{width:112px;height:8px;background:#fff;margin-bottom:3px;border-radius:1px}
.field.area{height:16px}
.send{display:inline-block;background:var(--green);font-size:5.5px;font-weight:700;padding:2px 7px;border-radius:2px}
.map{width:126px;height:56px;background:linear-gradient(135deg,#dfe6d9,#f2f2ea)}
.f-social{left:528px;top:1058px;display:flex;gap:8px}
.f-social span{width:12px;height:12px;border-radius:2px;background:#fff;opacity:.85}
.f-name{left:528px;top:1110px;color:#b9c7e3;font-family:"Open Sans",sans-serif;font-weight:700;font-size:9px}
.copy{left:0;top:1186px;width:771px;text-align:center;font-size:5.5px;color:#b9c7e3}
</style>
</head>
<body>

<header class="site-header abs">
  <div class="brand abs"><span class="brand-dot"></span><span class="brand-name">HSI<br>HARBOR SAFETY</span></div>
  <nav class="main-nav abs"><span>About Us</span><span>Class Calendar</span><span>Classes for Groups</span><span>Certification Cards</span><span>Policies</span></nav>
  <div class="social abs" style="left:622px"><span></span><span></span><span></span><span></span></div>
  <div class="header-contact abs"><span>info@harborsafety.com</span><b>(555) 240-7731</b></div>
</header>

<section class="hero abs" role="img" aria-label="Instructor guiding a student through CPR practice on a training manikin"></section>
<h1 class="hero-title abs">CPR+First Aid</h1>
<div class="hero-sub abs">FOR EVERYONE SINCE 2003</div>
<div class="hero-btn abs">Register Now</div>

<svg class="wave abs" width="771" height="80" viewBox="0 0 771 80">
  <path d="M0 20 Q385 60 771 20 L771 80 L0 80 Z" fill="var(--mist)"/>
  <path d="M0 28 Q385 66 771 28" fill="none" stroke="var(--green)" stroke-width="2"/>
</svg>
<div class="dots abs"><span></span><span></span><span></span></div>

<main class="content abs"></main>

<article class="card abs" style="left:120px">
  <div class="ph" role="img" aria-label="Group CPR class practicing compressions"></div>
  <h3>Group CPR + AED</h3>
  <p>Onsite group training for your staff with hands-on practice and same-day certification cards issued.</p>
  <span class="more">Read More »</span>
</article>
<article class="card abs" style="left:301px">
  <div class="ph" role="img" aria-label="Trainees learning first aid bandaging"></div>
  <h3>Group CPR + First Aid</h3>
  <p>Combined CPR and first aid course taught at your workplace by certified, experienced instructors.</p>
  <span class="more">Read More »</span>
</article>
<article class="card abs" style="left:482px">
  <div class="ph" role="img" aria-label="Healthcare providers in a BLS class"></div>
  <h3>Group BLS Healthcare CPR</h3>
  <p>Basic life support course for nurses, doctors and clinical teams meeting workplace requirements.</p>
  <span class="more">Read More »</span>
</article>

<section class="welcome abs">
  <h2>Welcome to <em>CPR Safety Classes</em></h2>
  <p><b>Harbor Safety Institute is Northern California's leader in CPR, BLS and First Aid certification classes, taught by experienced firefighters.</b></p>
  <p>Our instructors teach practical, confidence building skills in a friendly, professional setting. We train businesses, schools and individuals, and every class is led by experienced rescue professionals who keep lessons clear, active and focused on what matters most in an emergency. Students practice on modern manikins and leave ready to respond.</p>
  <p>Whether you need onsite training at your office or a seat in one of our weekly hosted classes, we make it easy to book, learn and leave certified the same day. Group rates are available for teams of any size across the region.</p>
  <span class="more">Read More »</span>
</section>

<aside class="testimonials abs">
  <h2>Client <em>Testimonials</em></h2>
  <div class="quote"><div class="avatar"></div><div><div class="quote-name">Dana Whitfield</div><div class="quote-role">Business Owner</div></div></div>
  <div class="bubble">"Our whole team was trained in one afternoon. Clear, friendly and professional from start to finish."</div>
</aside>

<section class="service abs" style="left:120px">
  <div class="ph" role="img" aria-label="Classroom set up with chairs and training manikins"></div>
  <div class="txt">
    <h3>Onsite</h3>
    <p><b>Harbor Safety Institute in Northern California</b></p>
    <p>We come to you. Training at your office or worksite taught by experienced firefighters and medics.</p>
    <span class="btn">Details</span>
  </div>
</section>
<section class="service abs" style="left:392px">
  <div class="ph" role="img" aria-label="Students practicing CPR in a hosted class"></div>
  <div class="txt">
    <h3>Hosted</h3>
    <p><b>Harbor Safety Institute in Northern California</b></p>
    <p>Weekly public classes at our two training centers. Reserve a seat and get certified the same day.</p>
    <span class="btn">Details</span>
  </div>
</section>

<footer class="site-footer abs"></footer>
<svg class="footer-wave abs" width="771" height="24" viewBox="0 0 771 24">
  <path d="M0 8 Q385 -6 771 8 L771 24 L0 24 Z" fill="var(--blue)"/>
</svg>
<div class="f-col abs" style="left:120px">
  <h4>Quick Links</h4>
  <ul class="f-links"><li>Home</li><li>About Us</li><li>Class Calendar</li><li>Classes for Groups</li><li>Certification Cards</li><li>Policies</li></ul>
</div>
<div class="f-col abs" style="left:238px">
  <h4>Quick Contact</h4>
  <div class="field"></div><div class="field"></div><div class="field area"></div>
  <span class="send">Send</span>
</div>
<div class="f-col abs" style="left:373px">
  <h4>Location Map</h4>
  <div class="map" role="img" aria-label="Street map of the training center location"></div>
</div>
<div class="f-social abs"><span></span><span></span><span></span><span></span></div>
<div class="f-name abs">Harbor Safety Institute</div>
<div class="copy abs">Copyright © 2024 Harbor Safety Institute. All rights reserved.</div>

</body>
</html>
```